Tirovel

We need a business card for our company is a holding for different business all are different we try to have some air of relax and fun in our projects we add pictures of the office to give you an idea od the mood of the business

Business

```html
<!DOCTYPE html>
<html lang="en">
<head>
<meta charset="utf-8">
<title>Tirovel — Business Card</title>
<link rel="stylesheet" href="https://fonts.googleapis.com/css2?family=Montserrat:wght@400;500;700&display=swap">
<style>
  :root {
    --backdrop: #e4e4e2;
    --sun-yellow: #f7ec37;
    --cocoa: #4a2a12;
    --charcoal: #2c2c2c;
    --paper: #ffffff;
    --ink: #1e1e1e;
    --card-w: 320px;
    --card-h: 540px;
    --radius: 26px;
  }
  * { box-sizing: border-box; margin: 0; padding: 0; }
  html, body {
    width: 1200px;
    height: 800px;
    overflow: hidden;
    background: var(--backdrop);
    font-family: "Montserrat", Arial, sans-serif;
  }
  .card-set {
    position: relative;
    width: 1200px;
    height: 800px;
    display: flex;
    justify-content: center;
    align-items: center;
    gap: 80px;
  }
  .card {
    width: var(--card-w);
    height: var(--card-h);
    border-radius: var(--radius);
    overflow: hidden;
    position: relative;
    box-shadow: 0 10px 26px rgba(0, 0, 0, 0.18);
  }

  /* Front side */
  .card-front {
    background: var(--sun-yellow);
    display: flex;
    flex-direction: column;
    align-items: center;
  }
  .brand-block {
    margin-top: 190px;
    display: flex;
    align-items: center;
    gap: 14px;
  }
  .brand-square {
    width: 30px;
    height: 30px;
    background: var(--cocoa);
  }
  .brand-name {
    font-weight: 700;
    font-size: 54px;
    letter-spacing: -1px;
    color: var(--cocoa);
    line-height: 1;
  }
  .front-rule {
    margin-top: 150px;
    width: 250px;
    height: 1px;
    background: rgba(74, 42, 18, 0.35);
  }
  .front-url {
    margin-top: 18px;
    font-weight: 700;
    font-size: 15px;
    letter-spacing: 3px;
    color: var(--cocoa);
  }

  /* Back side */
  .card-back {
    background: var(--paper);
  }
  .back-header {
    height: 300px;
    background: var(--charcoal);
    display: flex;
    align-items: center;
    justify-content: center;
  }
  .back-brand {
    font-weight: 700;
    font-size: 62px;
    letter-spacing: -1.5px;
    color: var(--paper);
  }
  .back-rule {
    height: 6px;
    background: var(--paper);
  }
  .name-band {
    height: 58px;
    background: var(--charcoal);
    display: flex;
    align-items: center;
    justify-content: center;
  }
  .person-name {
    font-weight: 700;
    font-size: 21px;
    letter-spacing: 2.5px;
    color: var(--sun-yellow);
    text-transform: uppercase;
  }
  .contact-list {
    list-style: none;
    padding-top: 40px;
    text-align: center;
    color: var(--ink);
    font-weight: 500;
    font-size: 20px;
    line-height: 1.55;
  }
</style>
</head>
<body>
  <main class="card-set">
    <section class="card card-front" aria-label="Card front">
      <div class="brand-block">
        <span class="brand-square"></span>
        <span class="brand-name">Tirovel</span>
      </div>
      <div class="front-rule"></div>
      <p class="front-url">WWW.TIROVEL.COM</p>
    </section>

    <section class="card card-back" aria-label="Card back">
      <div class="back-header">
        <span class="back-brand">Tirovel</span>
      </div>
      <div class="back-rule"></div>
      <div class="name-band">
        <span class="person-name">Mara Lindqvist</span>
      </div>
      <div class="back-rule"></div>
      <ul class="contact-list">
        <li class="contact-phone">555.014.2290</li>
        <li class="contact-email">mara@tirovel.com</li>
        <li class="contact-web">www.tirovel.com</li>
      </ul>
    </section>
  </main>
</body>
</html>
```